Email Signatures

I would like to create a new email signature for my team. The design will be the same for everyone, with only individual details such as name and email changing. You can also see our brand style on our website. https://www.tlmbespokehomes.com.au/

Target Market(s)

Clients for new builds or renovations

Industry/Entity Type

Construction

Colors

Designer to choose colors to be used in the design.

```html
<!DOCTYPE html>
<html lang="en">
<head>
<meta charset="utf-8">
<title>TLM Bespoke Homes – Email Signature</title>
<link href="https://fonts.googleapis.com/css2?family=Nunito+Sans:wght@400;700;800&display=swap" rel="stylesheet">
<style>
  :root {
    --brand-green: #138a36;
    --ink: #1c1c1c;
    --muted: #7a7a7a;
    --fine: #8a8a8a;
    --rule: #e2e2e2;
    --page: #ffffff;
  }
  * { box-sizing: border-box; margin: 0; padding: 0; }
  html, body {
    width: 1200px; height: 800px; overflow: hidden;
    background: var(--page);
    font-family: "Nunito Sans", Arial, sans-serif;
  }
  .signature {
    position: absolute;
    left: 110px; top: 200px;
    width: 980px;
    border-top: 4px solid var(--brand-green);
  }
  .signature-main {
    display: flex;
    align-items: center;
    padding: 36px 0 34px 36px;
  }
  .brand-mark {
    width: 250px;
    display: flex;
    align-items: center;
    gap: 12px;
  }
  .brand-mark .square {
    width: 22px; height: 22px;
    background: var(--brand-green);
    flex-shrink: 0;
  }
  .brand-name {
    font-weight: 800;
    font-size: 25px;
    line-height: 1.15;
    color: var(--ink);
  }
  .divider {
    width: 2px; height: 120px;
    background: var(--brand-green);
    margin: 0 32px 0 22px;
  }
  .details { line-height: 1; }
  .person-name { font-size: 27px; font-weight: 700; color: var(--ink); }
  .person-role { font-size: 21px; color: var(--muted); margin-top: 10px; }
  .contact { margin-top: 22px; font-size: 21px; color: var(--brand-green); }
  .contact a { color: inherit; text-decoration: none; }
  .contact p + p { margin-top: 12px; }
  .location { font-size: 20px; color: var(--muted); margin-top: 16px; }
  .social { display: flex; gap: 14px; margin-top: 16px; }
  .social span {
    width: 22px; height: 22px; border-radius: 3px;
    background: var(--ink);
  }
  .disclaimer {
    border-top: 2px solid var(--rule);
    padding-top: 18px;
    font-size: 17px;
    line-height: 1.6;
    color: var(--fine);
  }
</style>
</head>
<body>
  <section class="signature">
    <div class="signature-main">
      <div class="brand-mark">
        <span class="square"></span>
        <span class="brand-name">TLM Bespoke<br>Homes</span>
      </div>
      <div class="divider"></div>
      <div class="details">
        <h1 class="person-name">Dean Whitfield</h1>
        <p class="person-role">General Manager</p>
        <div class="contact">
          <p>0400 512 738</p>
          <p><a href="mailto:info@tlmbespokehomes.com.au">info@tlmbespokehomes.com.au</a></p>
        </div>
        <p class="location">Ridgeview, Marlow Coast, Australia</p>
        <div class="social" aria-label="Social links">
          <span></span><span></span>
        </div>
      </div>
    </div>
    <p class="disclaimer">This email and any attachments are confidential and intended solely for the use of the individual or entity to whom they are addressed. If you have received this email in error, please notify the sender and delete it from your system. Any unauthorised use, disclosure, or copying is prohibited.</p>
  </section>
</body>
</html>
```